VMR business card

Need a business card for a company that provides instructional design and elearning development services. The website is here: http://vantmoro.studio/

I'm attaching a current logo, as well as the old business card design. While I like to keep it clean, the old design is too simplistic for my liking. The only idea I want to reuse from the old design is placing industry jargon on the back of the card, just need a better way to present it. But if you have other ideas for the back--feel free to experiment.

Please use the colors complementary to the color we have on the website. Thank you!

```html
<!DOCTYPE html>
<html lang="en">
<head>
<meta charset="utf-8">
<title>VMR business card</title>
<link href="https://fonts.googleapis.com/css2?family=Montserrat:wght@700;800&family=Oswald:wght@500&family=Lato:wght@400;700&display=swap" rel="stylesheet">
<style>
  :root {
    --stage: #e9e6e1;
    --card-dark: #27272b;
    --card-black: #0f0f10;
    --band-white: #f4f4f4;
    --teal: #1ba595;
    --teal-light: #4fc3c0;
    --gold: #cbbd8f;
    --white: #ffffff;
    --logo-grey: #3a3a3a;
  }
  * { box-sizing: border-box; margin: 0; padding: 0; }
  html, body { width: 1200px; height: 900px; overflow: hidden; }
  body { background: var(--stage); position: relative; }

  .card {
    position: absolute;
    width: 600px;
    height: 343px;
    overflow: hidden;
    box-shadow: 0 12px 30px rgba(0,0,0,.25);
  }

  /* Back of card: jargon wall */
  .card-back {
    left: 70px; top: 70px;
    background: var(--card-dark);
    border-radius: 0 46px 0 46px;
    padding: 26px 0 0 30px;
  }
  .jargon {
    font-family: "Montserrat", sans-serif;
    font-weight: 800;
    color: var(--teal);
    font-size: 31px;
    line-height: 40px;
    letter-spacing: 1px;
    white-space: nowrap;
  }
  .headline-row {
    display: flex;
    align-items: center;
    margin: 2px 0 2px -30px;
    height: 56px;
  }
  .headline-bar { width: 14px; height: 34px; background: var(--white); }
  .headline {
    font-family: "Oswald", sans-serif;
    font-weight: 500;
    color: var(--white);
    font-size: 60px;
    letter-spacing: -2px;
    line-height: 1;
    margin: 0 10px;
    white-space: nowrap;
  }

  /* Front of card: identity */
  .card-front {
    left: 530px; top: 487px;
    background: var(--card-black);
    border-radius: 46px 0 46px 0;
  }
  .brand-band {
    height: 92px;
    background: var(--band-white);
    display: flex;
    align-items: center;
    padding-left: 34px;
    gap: 12px;
  }
  .brand-dot { width: 30px; height: 30px; border-radius: 50%; background: var(--teal); }
  .brand-name {
    font-family: "Lato", sans-serif;
    font-weight: 700;
    font-size: 38px;
    color: var(--teal);
    letter-spacing: 2px;
  }
  .contact { padding: 70px 0 0 42px; font-family: "Lato", sans-serif; }
  .contact-name { color: var(--teal-light); font-weight: 700; font-size: 21px; margin-bottom: 12px; }
  .contact-line {
    display: flex; align-items: center; gap: 10px;
    color: var(--gold); font-size: 17px; line-height: 26px;
    padding-left: 12px;
  }
  .contact-line svg { width: 15px; height: 15px; flex: none; }
</style>
</head>
<body>

<section class="card card-back" aria-label="Card back">
  <p class="jargon">MOBILE LEARNING SCORM</p>
  <p class="jargon">INSTRUCTIONAL DESIGN LMS</p>
  <p class="jargon">MOOCS ELEARNING HTML5</p>
  <div class="headline-row">
    <span class="headline-bar"></span>
    <span class="headline">HOW CAN WE HELP?</span>
    <span class="headline-bar"></span>
  </div>
  <p class="jargon">ADULT LEARNING THEORY</p>
  <p class="jargon">GAMIFICATION CLASSROOM</p>
  <p class="jargon">XAPI BLENDED LEARNING</p>
</section>

<section class="card card-front" aria-label="Card front">
  <div class="brand-band">
    <span class="brand-dot"></span>
    <span class="brand-name">VMR</span>
  </div>
  <div class="contact">
    <p class="contact-name">Dana Whitlock</p>
    <p class="contact-line">
      <svg viewBox="0 0 16 16"><path fill="var(--teal)" d="M3.5 1l2.5 3-1.5 2c1 2 3 4 5 5l2-1.5 3 2.5-1.5 2.5C7 15 1 9 1 2.5z"/></svg>
      555-014-2280
    </p>
    <p class="contact-line">
      <svg viewBox="0 0 16 16"><rect x="1" y="3" width="14" height="10" fill="none" stroke="var(--teal)" stroke-width="1.6"/><path d="M1 3l7 6 7-6" fill="none" stroke="var(--teal)" stroke-width="1.6"/></svg>
      dwhitlock@vantmoro.studio
    </p>
    <p class="contact-line">
      <svg viewBox="0 0 16 16" fill="none" stroke="var(--teal)" stroke-width="1.4"><circle cx="8" cy="8" r="6.5"/><ellipse cx="8" cy="8" rx="2.8" ry="6.5"/><path d="M1.5 8h13M2.5 5h11M2.5 11h11"/></svg>
      www.vantmoro.studio
    </p>
  </div>
</section>

</body>
</html>
```